Create a professional, eye-catching business card design that reflects the values and services of Brookfern Veterinary Hospital. we provide veterinary services and the business card should be a memorable representation of the clinic and align with its branding and mission. our tag line is "Life Long Companions, Lifelong Care"
Use clean, modern typography. Prioritize readability and professionalism. We would like to see designs that use the color blue, as in the logo example. the final design should communicate professionalism and care, with attention to detail.

```html
<!DOCTYPE html>
<html lang="en">
<head>
<meta charset="utf-8">
<title>Brookfern Veterinary Hospital – Business Card</title>
<link rel="stylesheet" href="https://fonts.googleapis.com/css2?family=Lato:wght@400;700;900&family=Montserrat:wght@300;400;600&display=swap">
<style>
  :root {
    --stage: #1b1b1b;
    --blue-light: #2f5698;
    --blue-deep: #1b3770;
    --navy: #1d3461;
    --paper: #ececec;
    --white: #ffffff;
    --text-dark: #1e1e1e;
    --rule: #8a8a8a;
  }
  * { margin: 0; padding: 0; box-sizing: border-box; }
  html, body { width: 1200px; height: 1000px; overflow: hidden; }
  body { background: var(--stage); position: relative; font-family: "Lato", sans-serif; }

  .card {
    position: absolute; left: 225px; width: 750px; height: 427px;
    border-radius: 26px; overflow: hidden;
  }
  .card-front {
    top: 60px;
    background: radial-gradient(ellipse at 45% 30%, var(--blue-light) 0%, #284b8a 45%, var(--blue-deep) 100%);
    color: var(--white);
  }
  .ornament-area {
    position: absolute; left: 210px; top: -90px; width: 310px; height: 182px;
    border-radius: 0 0 160px 160px;
    background: radial-gradient(ellipse at 50% 30%, rgba(255,255,255,0.10), rgba(255,255,255,0.02));
  }
  .tagline {
    position: absolute; left: 158px; top: 190px;
    display: flex; align-items: baseline;
    font-family: "Montserrat", sans-serif;
  }
  .tagline-lead { font-size: 28px; font-weight: 300; letter-spacing: 1px; }
  .tagline-text {
    margin-left: 12px; padding-bottom: 6px;
    border-bottom: 1.5px solid var(--white);
    font-size: 16.5px; font-weight: 400; letter-spacing: 0.3px;
  }
  .tagline-text strong { font-weight: 600; }

  .brand-block {
    position: absolute; display: flex; flex-direction: column; align-items: center;
    font-family: "Lato", sans-serif; font-weight: 900; line-height: 1;
  }
  .brand-dot { border-radius: 50%; }
  .brand-name .word { display: block; text-align: center; letter-spacing: 0.5px; }
  .brand-name .sub { display: block; text-align: center; letter-spacing: 0.6px; }

  .card-front .brand-block { right: 40px; top: 282px; width: 200px; color: var(--white); }
  .card-front .brand-dot { width: 80px; height: 80px; background: rgba(255,255,255,0.9); margin-bottom: 10px; }
  .card-front .brand-name .word { font-size: 27px; }
  .card-front .brand-name .sub { font-size: 10px; margin-top: 3px; }

  .card-back { top: 514px; background: var(--paper); color: var(--navy); }
  .card-back .brand-block { left: 77px; top: 128px; width: 220px; color: var(--navy); }
  .card-back .brand-dot { width: 96px; height: 96px; background: var(--navy); margin-bottom: 14px; }
  .card-back .brand-name .word { font-size: 32px; }
  .card-back .brand-name .sub { font-size: 12.5px; margin-top: 4px; }

  .divider { position: absolute; left: 352px; top: 77px; width: 1px; height: 274px; background: var(--rule); }
  .contact { position: absolute; left: 429px; top: 106px; }
  .person-name { font-weight: 700; font-size: 27px; color: var(--navy); line-height: 1; }
  .person-org { font-size: 16.5px; color: var(--text-dark); margin-top: 8px; }
  .details { list-style: none; margin-top: 24px; font-size: 15px; color: var(--text-dark); }
  .details li { display: flex; align-items: flex-start; margin-bottom: 7px; line-height: 18px; }
  .details svg { width: 14px; height: 14px; margin: 2px 14px 0 1px; flex: none; fill: var(--navy); }
  .details .address { line-height: 18px; margin-left: -1px; }
  .base-band {
    position: absolute; left: 40px; right: 40px; bottom: 0; height: 12px;
    background: var(--navy); border-radius: 40px 40px 0 0;
  }
</style>
</head>
<body>
  <section class="card card-front">
    <div class="ornament-area" role="img" aria-label="Botanical sprig with seed pods on a thin arc"></div>
    <div class="tagline">
      <span class="tagline-lead">LIFELONG</span>
      <span class="tagline-text">COMPANIONS, LIFELONG <strong>CARE</strong></span>
    </div>
    <div class="brand-block">
      <div class="brand-dot"></div>
      <div class="brand-name"><span class="word">BROOKFERN</span><span class="sub">VETERINARY HOSPITAL</span></div>
    </div>
  </section>

  <section class="card card-back">
    <div class="brand-block">
      <div class="brand-dot"></div>
      <div class="brand-name"><span class="word">BROOKFERN</span><span class="sub">VETERINARY HOSPITAL</span></div>
    </div>
    <div class="divider"></div>
    <div class="contact">
      <h1 class="person-name">DR. CLARA WENDT</h1>
      <p class="person-org">Brookfern Veterinary Hospital</p>
      <ul class="details">
        <li><svg viewBox="0 0 24 24"><path d="M6.6 10.8a15.1 15.1 0 0 0 6.6 6.6l2.2-2.2c.3-.3.7-.4 1-.2 1.1.4 2.3.6 3.6.6.6 0 1 .4 1 1V20c0 .6-.4 1-1 1A17 17 0 0 1 3 4c0-.6.4-1 1-1h3.5c.6 0 1 .4 1 1 0 1.3.2 2.5.6 3.6.1.3 0 .7-.2 1z"/></svg>044-987 654 321</li>
        <li><svg viewBox="0 0 24 24"><path d="M2 5h20v14H2z"/><path d="M2 5l10 7 10-7v2l-10 7L2 7z" fill="#ececec"/></svg>hello@brookfernvet.com</li>
        <li><svg viewBox="0 0 24 24"><path d="M12 2a10 10 0 1 0 0 20 10 10 0 0 0 0-20zm6.9 6h-2.9a15.7 15.7 0 0 0-1.4-3.6A8 8 0 0 1 18.9 8zM12 4c.8 1.2 1.5 2.5 1.9 4h-3.8c.4-1.5 1.1-2.8 1.9-4zM4.3 14a8 8 0 0 1 0-4h3.4a16 16 0 0 0 0 4zm.8 2h2.9c.3 1.3.8 2.5 1.4 3.6A8 8 0 0 1 5.1 16zM8 8H5.1a8 8 0 0 1 4.3-3.6C8.8 5.5 8.3 6.7 8 8zm4 12c-.8-1.2-1.5-2.5-1.9-4h3.8c-.4 1.5-1.1 2.8-1.9 4zm2.3-6H9.7a14.7 14.7 0 0 1 0-4h4.6a14.7 14.7 0 0 1 0 4zm.3 5.6c.6-1.1 1.1-2.3 1.4-3.6h2.9a8 8 0 0 1-4.3 3.6zm1.7-5.6a16 16 0 0 0 0-4h3.4a8 8 0 0 1 0 4z"/></svg>www.brookfernvet.com</li>
        <li><svg viewBox="0 0 24 24"><path d="M12 2a7 7 0 0 0-7 7c0 5.2 7 13 7 13s7-7.8 7-13a7 7 0 0 0-7-7zm0 9.5a2.5 2.5 0 1 1 0-5 2.5 2.5 0 0 1 0 5z"/></svg><span class="address">412 Elm Ridge Rd<br>Oakdale, FL 33520,<br>2250 Harbor View Ave<br>Lakeview, FL 33915</span></li>
      </ul>
    </div>
    <div class="base-band"></div>
  </section>
</body>
</html>
```